TR Advisory Business Cards - High End AV / Low Voltage Company

We are low voltage AV company that specializes in high end clients on the residential side and larger businesses on the commercial side. We want something modern, tech looking but also something that is extremely professional looking. We have uploaded our logos and postcards we already have in the field. Along with a picture of one of our wrapped vans. Our website is at www.trvadvisory.example and our primary colors are the orange, green, grey and blue all military color finishes.

We are interesting in the slogans "Connecting You with Smarter Technology" or "Leading the Lowcountry in Tech"

Target Market(s)

We focus on 70% Commercial and 30% Residential Customers

Industry/Entity Type

Low Voltage, AV Company

Contact Information for Business Card

Name - Dorian Fairweather, Title - Owner, Office Phone - 555-714-3096, Mobile Phone - 555-802-4173, E-Mail - d@trvadvisory.example, Website: www.trvadvisory.example

Font styles to use
Sans Serif

Requirements
Must have
• Must have Name, Title, Work Phone & Mobile, Website and Logo.
Nice to have
• We want something that will impress our higher end clients with a great logo
Should not have
• Too traditional or plain.

```html
<!DOCTYPE html>
<html lang="en">
<head>
<meta charset="utf-8">
<title>TR Advisory Business Cards</title>
<link rel="stylesheet" href="https://fonts.googleapis.com/css2?family=Jost:wght@400;500&display=swap">
<style>
  :root {
    --backdrop: #c6c6c6;
    --card: #ffffff;
    --orange: #ec6836;
    --olive: #404823;
    --ink: #3d4520;
    --grey-text: #555a50;
    --pattern-light: #fbfbfb;
    --pattern-mid: #f3f3f3;
  }
  * { margin: 0; padding: 0; box-sizing: border-box; }
  html, body { width: 1200px; height: 1200px; overflow: hidden; }
  body {
    background: var(--backdrop);
    font-family: "Jost", "Futura", sans-serif;
    position: relative;
  }
  .card {
    position: absolute;
    left: 226px;
    width: 750px;
    background: var(--card);
    overflow: hidden;
  }
  .card-front { top: 92px; height: 458px; }
  .card-back { top: 633px; height: 457px; }

  /* Front */
  .front-pattern {
    position: absolute; left: 0; top: 0; width: 750px; height: 363px;
    background: radial-gradient(ellipse at center, var(--card) 35%, var(--pattern-light) 65%, var(--pattern-mid) 100%);
  }
  .front-band {
    position: absolute; left: 0; top: 363px; width: 750px; height: 95px;
    background: var(--olive);
  }
  .brand-mark {
    position: absolute; left: 350px; top: 130px;
    width: 50px; height: 50px; border-radius: 50%;
    background: var(--orange);
  }
  .brand-name {
    position: absolute; left: 0; top: 222px; width: 750px;
    text-align: center;
    color: var(--orange);
    font-weight: 500;
    font-size: 58px;
    letter-spacing: 3px;
    line-height: 1;
  }
  .tagline {
    position: absolute; left: 86px; top: 340px;
    width: 578px; height: 51px;
    background: var(--orange);
    border: 2px solid var(--card);
    border-radius: 26px;
    color: #fff;
    font-weight: 500;
    font-size: 21.5px;
    display: flex; align-items: center; justify-content: center;
    letter-spacing: 0.2px;
    white-space: nowrap;
  }

  /* Back */
  .holder-name {
    position: absolute; left: 57px; top: 46px;
    font-weight: 500; font-size: 32px; color: var(--ink);
    line-height: 1;
    white-space: nowrap;
  }
  .name-rule {
    position: absolute; left: 0; top: 84px; width: 332px; height: 2px;
    background: var(--orange);
  }
  .name-rule::before {
    content: ""; position: absolute; left: 0; top: -2px; width: 54px; height: 6px;
    background: var(--orange);
  }
  .holder-title {
    position: absolute; left: 57px; top: 90px;
    font-size: 25px; color: var(--grey-text); line-height: 1.1;
  }
  .van-photo {
    position: absolute; left: 60px; top: 143px;
    width: 180px; height: 180px; border-radius: 50%;
    border: 4px solid var(--orange);
    background: linear-gradient(180deg, #7d8a4a 0%, #3f4a26 45%, #4a5030 70%, #8a8a80 100%);
  }
  .contact-list {
    position: absolute; left: 374px; top: 134px;
    list-style: none;
  }
  .contact-item {
    display: flex; align-items: center;
    height: 48.7px;
    font-size: 25px; color: var(--ink);
    white-space: nowrap;
  }
  .contact-icon {
    width: 38px; height: 38px; margin-right: 20px; flex: none;
  }
  .back-rule {
    position: absolute; left: 0; top: 359px; width: 750px; height: 3px;
    background: var(--orange);
  }
  .back-band {
    position: absolute; left: 0; top: 362px; width: 750px; height: 95px;
    background: var(--olive);
  }
</style>
</head>
<body>
  <section class="card card-front">
    <div class="front-pattern" role="img" aria-label="Faint circuit-trace background pattern"></div>
    <div class="brand-mark"></div>
    <div class="brand-name">TR ADVISORY</div>
    <div class="front-band"></div>
    <div class="tagline">CONNECTING YOU WITH SMARTER TECHNOLOGY</div>
  </section>

  <section class="card card-back">
    <h1 class="holder-name">Dorian Fairweather</h1>
    <div class="name-rule"></div>
    <p class="holder-title">Owner</p>
    <div class="van-photo" role="img" aria-label="Photo of the company's wrapped service van parked outdoors"></div>

    <ul class="contact-list">
      <li class="contact-item">
        <svg class="contact-icon" viewBox="0 0 38 38" aria-hidden="true">
          <circle cx="19" cy="19" r="19" fill="#ec6836"/>
          <path d="M13 10c1-1 2.5-1 3 .3l1.6 3.6c.4.9 0 1.8-.7 2.3l-1 .7c.9 2.3 2.6 4.2 4.9 5.3l.8-1c.6-.7 1.5-.9 2.3-.5l3.4 1.7c1.1.6 1.2 2 .3 3l-1.4 1.5c-1 1-2.6 1.2-4 .6C16.6 25.3 12 20.6 10.4 15c-.4-1.5 0-3 1-4z" fill="#fff"/>
        </svg>
        <span>555-714-3096</span>
      </li>
      <li class="contact-item">
        <svg class="contact-icon" viewBox="0 0 38 38" aria-hidden="true">
          <circle cx="19" cy="19" r="19" fill="#ec6836"/>
          <rect x="13" y="8.5" width="12" height="21" rx="2" fill="none" stroke="#fff" stroke-width="2"/>
          <line x1="17" y1="26" x2="21" y2="26" stroke="#fff" stroke-width="1.8"/>
        </svg>
        <span>555-802-4173</span>
      </li>
      <li class="contact-item">
        <svg class="contact-icon" viewBox="0 0 38 38" aria-hidden="true">
          <circle cx="19" cy="19" r="19" fill="#ec6836"/>
          <rect x="9.5" y="12.5" width="19" height="13" fill="none" stroke="#fff" stroke-width="1.8"/>
          <path d="M9.5 12.5l9.5 8 9.5-8M9.5 25.5l7-6M28.5 25.5l-7-6" fill="none" stroke="#fff" stroke-width="1.6"/>
        </svg>
        <span>d@trvadvisory.example</span>
      </li>
      <li class="contact-item">
        <svg class="contact-icon" viewBox="0 0 38 38" aria-hidden="true">
          <circle cx="19" cy="19" r="19" fill="#ec6836"/>
          <g fill="none" stroke="#fff" stroke-width="1.6">
            <circle cx="19" cy="19" r="10"/>
            <ellipse cx="19" cy="19" rx="4.5" ry="10"/>
            <line x1="9" y1="19" x2="29" y2="19"/>
            <line x1="10.5" y1="14" x2="27.5" y2="14"/>
            <line x1="10.5" y1="24" x2="27.5" y2="24"/>
          </g>
        </svg>
        <span>www.trvadvisory.example</span>
      </li>
    </ul>

    <div class="back-rule"></div>
    <div class="back-band"></div>
  </section>
</body>
</html>
```